Professional Home Buyer business card needed

I need a pretty straight forward business card designed. We help people that NEED to sell their homes solve problems. We perform all types of Real Estate transactions including flip, wholesale, investment, rental property and multi family. The card will mainly be used to give to prospective Sellers but will also be given to Real Estate Investors as well. It should professional and very easy to read, most clients are older people.

Target Market(s)

Distressed home sellers as well as Real Estate investors

Industry/Entity Type

Real Estate

Contact Information for Business Card

should be a professional layout

Colors
ec1f27
ffffff
000000

Requirements
Must have
• Large logo on back and smaller one on front. should utilize Red, white, and black.
• I am thinking of using a soft touch coating on the card so keep that in mind.
• Contact info should be very easy to read, think older clients.
Nice to have
• I would like to see a design with rounded corners on the card
Should not have
• pictures of homes or other home graphics.

```html
<!DOCTYPE html>
<html lang="en">
<head>
<meta charset="utf-8">
<title>Plainside Home Buyers — Business Card</title>
<link href="https://fonts.googleapis.com/css2?family=Montserrat:wght@400;500;600;800&display=swap" rel="stylesheet">
<style>
  :root {
    --brand-red: #ec1f27;
    --ink: #1d1f21;
    --ink-soft: #4a4d50;
    --muted: #8a8d90;
    --paper: #f4f4f3;
    --slate-top: #45494d;
    --slate-bottom: #2e3134;
    --stage: #d9d9d7;
  }
  * { box-sizing: border-box; margin: 0; padding: 0; }
  html, body {
    width: 1200px; height: 900px; overflow: hidden;
    background: var(--stage);
    font-family: "Montserrat", Arial, sans-serif;
  }
  .sheet {
    width: 1200px; height: 900px;
    display: flex; flex-direction: column;
    align-items: center; justify-content: center; gap: 44px;
  }
  .card {
    width: 672px; height: 384px;
    box-shadow: 0 6px 18px rgba(0,0,0,.18);
    position: relative;
  }

  /* Back side */
  .card--back {
    background: linear-gradient(160deg, var(--slate-top), var(--slate-bottom));
    display: flex; align-items: center; justify-content: center;
  }
  .brand-lockup {
    display: flex; align-items: center; gap: 16px;
  }
  .brand-dot {
    width: 22px; height: 22px; background: var(--brand-red); border-radius: 50%;
  }
  .brand-name {
    font-weight: 800; letter-spacing: 2px; text-transform: uppercase;
    line-height: 1.05;
  }
  .card--back .brand-name { color: #ffffff; font-size: 44px; }

  /* Front side */
  .card--front {
    background: var(--paper);
    display: flex; align-items: center;
    padding: 0 40px 0 56px;
  }
  .front-brand {
    width: 228px;
    display: flex; align-items: center; gap: 10px;
  }
  .front-brand .brand-dot { width: 14px; height: 14px; flex: none; }
  .card--front .brand-name { color: var(--ink); font-size: 22px; letter-spacing: 1px; }
  .divider {
    width: 2px; height: 150px; background: var(--brand-red);
    margin: 0 34px 0 20px;
  }
  .person-name {
    color: var(--brand-red); font-weight: 600; font-size: 25px; letter-spacing: .5px;
  }
  .person-title {
    color: var(--muted); font-weight: 500; font-size: 19px; margin-top: 2px;
  }
  .contact-list { list-style: none; margin-top: 26px; }
  .contact-item {
    display: flex; align-items: center; gap: 16px;
    color: var(--ink-soft); font-size: 17px; font-weight: 500;
    margin-bottom: 11px;
  }
  .contact-icon { width: 18px; height: 18px; flex: none; }
</style>
</head>
<body>
<main class="sheet">
  <section class="card card--back" aria-label="Card back">
    <div class="brand-lockup">
      <span class="brand-dot"></span>
      <span class="brand-name">Plainside<br>Home Buyers</span>
    </div>
  </section>

  <section class="card card--front" aria-label="Card front">
    <div class="front-brand">
      <span class="brand-dot"></span>
      <span class="brand-name">Plainside<br>Home Buyers</span>
    </div>
    <div class="divider"></div>
    <div class="contact-block">
      <h1 class="person-name">Dana Whitfield</h1>
      <p class="person-title">President</p>
      <ul class="contact-list">
        <li class="contact-item">
          <svg class="contact-icon" viewBox="0 0 24 24"><path fill="#ec1f27" d="M6.6 10.8a15.1 15.1 0 0 0 6.6 6.6l2.2-2.2a1 1 0 0 1 1-.25 11.4 11.4 0 0 0 3.6.57 1 1 0 0 1 1 1V20a1 1 0 0 1-1 1A17 17 0 0 1 3 4a1 1 0 0 1 1-1h3.5a1 1 0 0 1 1 1c0 1.25.2 2.45.57 3.6a1 1 0 0 1-.25 1z"/></svg>
          316-555-0148
        </li>
        <li class="contact-item">
          <svg class="contact-icon" viewBox="0 0 24 24"><rect x="2" y="5" width="20" height="14" fill="#ec1f27"/><path d="M2 5l10 8 10-8" fill="none" stroke="#f4f4f3" stroke-width="1.6"/></svg>
          dana@plainsidehomebuyers.com
        </li>
        <li class="contact-item">
          <svg class="contact-icon" viewBox="0 0 24 24" fill="none" stroke="#ec1f27" stroke-width="1.8"><circle cx="12" cy="12" r="9.5"/><ellipse cx="12" cy="12" rx="4" ry="9.5"/><path d="M2.5 12h19M4 7h16M4 17h16"/></svg>
          www.plainsidehomebuyers.com
        </li>
      </ul>
    </div>
  </section>
</main>
</body>
</html>
```